BrivoPeak Business Card Design Project

We are looking for a modern, clean business card design for our new company. We are a consulting firm focused on the financial services market providing management and IT consulting to banks, insurance companies, etc. Please include our company logo and company contact information from the attached file in the design. Two versions of the logo are attached, either version is acceptable. Logos are available in other file formats if needed. We would like to include the contact information for both our UK and US offices as well as the following information for each individual card holder: Name, position/title, address, phone number and e-mail address.
Updates
Project Deadline Extended
Reason: A last minute trip over seas has prevented us from finalizing the decision. A decision will be made this week. We apologize for the inconvenience.
Industry/Entity Type
Business
Contact Information for Business Card
Company logo.
Company locations and phone numbers for both the US and UK offices.
Company URL.
Cardholder Name
Cardholder Position/title
Cardholder Address
Cardholder Phone Number
Cardholder e-mail Address
Look and feel
Each slider illustrates characteristics of the customer's brand and the style your logo design should communicate.

```html
<!DOCTYPE html>
<html lang="en">
<head>
<meta charset="utf-8">
<title>BrivoPeak Partners – Business Card</title>
<link href="https://fonts.googleapis.com/css2?family=Open+Sans:wght@400;600;700&display=swap" rel="stylesheet">
<style>
  :root {
    --backdrop: #e9e7e3;
    --card: #f7f7f7;
    --navy: #253a5e;
    --ink: #1c1c1c;
    --rule: #2a2a2a;
  }
  * { margin: 0; padding: 0; box-sizing: border-box; }
  html, body { width: 1200px; height: 902px; overflow: hidden; }
  body {
    background: var(--backdrop);
    font-family: "Open Sans", sans-serif;
    display: flex; align-items: center; justify-content: center;
  }
  .card {
    position: relative;
    width: 1000px; height: 572px;
    background: var(--card);
    box-shadow: 0 6px 24px rgba(0,0,0,.18);
  }
  .brand {
    position: absolute; left: 70px; top: 80px;
    display: flex; align-items: center; gap: 20px;
  }
  .brand-mark { width: 56px; height: 56px; background: var(--navy); flex: none; }
  .brand-name {
    color: var(--navy); font-weight: 700; font-size: 50px; line-height: 1;
    letter-spacing: -1px; white-space: nowrap;
  }
  .holder-line {
    position: absolute; left: 580px; right: 280px; top: 186px;
    height: 2px; background: var(--rule);
  }
  .holder {
    position: absolute; right: 70px; top: 138px; text-align: right;
    white-space: nowrap;
  }
  .holder-name { color: var(--navy); font-size: 34px; font-weight: 400; line-height: 1.2; }
  .holder-title { color: var(--ink); font-size: 20px; font-weight: 600; margin-top: 2px; }
  .rule {
    position: absolute; left: 70px; right: 70px; top: 240px;
    height: 2px; background: var(--rule);
  }
  .contacts {
    position: absolute; left: 70px; top: 272px; list-style: none;
  }
  .contacts li {
    display: flex; align-items: center; gap: 16px;
    font-size: 23px; color: var(--ink); height: 42px; white-space: nowrap;
  }
  .icon {
    width: 26px; height: 26px; background: var(--navy);
    display: flex; align-items: center; justify-content: center; flex: none;
  }
  .icon svg { width: 18px; height: 18px; }
</style>
</head>
<body>
  <div class="card">
    <div class="brand">
      <div class="brand-mark"></div>
      <div class="brand-name">BrivoPeak Partners</div>
    </div>

    <div class="holder-line"></div>
    <div class="holder">
      <div class="holder-name">Jonah Rowan</div>
      <div class="holder-title">Managing Director</div>
    </div>

    <div class="rule"></div>

    <ul class="contacts">
      <li>
        <span class="icon"><svg viewBox="0 0 20 20"><path d="M5 3h3l1 4-2 1a9 9 0 0 0 5 5l1-2 4 1v3c0 1-1 2-2 2A13 13 0 0 1 3 5c0-1 1-2 2-2z" fill="#fff"/></svg></span>
        US: (555) 014-2290
      </li>
      <li>
        <span class="icon"><svg viewBox="0 0 20 20"><path d="M5 3h3l1 4-2 1a9 9 0 0 0 5 5l1-2 4 1v3c0 1-1 2-2 2A13 13 0 0 1 3 5c0-1 1-2 2-2z" fill="#fff"/></svg></span>
        UK: +44 7700 900412
      </li>
      <li>
        <span class="icon"><svg viewBox="0 0 20 20" fill="none" stroke="#fff" stroke-width="1.6"><circle cx="10" cy="10" r="7"/><ellipse cx="10" cy="10" rx="3" ry="7"/><path d="M3 10h14"/></svg></span>
        www.brivopeakpartners.com
      </li>
      <li>
        <span class="icon"><svg viewBox="0 0 20 20" fill="none" stroke="#fff" stroke-width="1.6"><rect x="3" y="5" width="14" height="10"/><path d="M3 5l7 6 7-6"/></svg></span>
        jrowan@brivopeakpartners.com
      </li>
      <li>
        <span class="icon"><svg viewBox="0 0 20 20"><path d="M10 2a5 5 0 0 0-5 5c0 4 5 11 5 11s5-7 5-11a5 5 0 0 0-5-5zm0 7a2 2 0 1 1 0-4 2 2 0 0 1 0 4z" fill="#fff"/></svg></span>
        14 Harrow Lane&nbsp; London E2 4PL Great Britain
      </li>
      <li>
        <span class="icon"><svg viewBox="0 0 20 20"><path d="M10 2a5 5 0 0 0-5 5c0 4 5 11 5 11s5-7 5-11a5 5 0 0 0-5-5zm0 7a2 2 0 1 1 0-4 2 2 0 0 1 0 4z" fill="#fff"/></svg></span>
        218 N Alder St, Suite 204 Fairview UT 84088 United States
      </li>
    </ul>
  </div>
</body>
</html>
```